Velmora Commercial Finance Information Brochure

This brochure will be sent out to clients via A4 PDF on an email to showcase what our company has to offer. We are a commercial finance brokerage, that specialises in property finance. We would like to see designs following our colour scheme. The final design should demonstrate our professionalism and reliability.
I have attached our logo and also a few bullet points on our information and what we can offer. These can be slightly reworded for conciseness. Or leave the text sections as filler and I can fill these in.
I have also attached an overview of our colour scheme and design styling for your consideration.
Target Market(s)
Property Developers
Industry/Entity Type
Financial Services
Look and feel
Each slider illustrates characteristics of the customer's brand and the style your logo design should communicate.

```html
<!DOCTYPE html>
<html lang="en">
<head>
<meta charset="utf-8">
<title>Velmora Commercial Finance – Brochure Cover</title>
<link rel="stylesheet" href="https://fonts.googleapis.com/css2?family=Montserrat:wght@700;800&display=swap">
<style>
  :root {
    --stage: #d1d0d3;
    --paper: #f4f4f5;
    --brand-blue: #0d3fa6;
    --brand-green: #1c8a3a;
    --text-light: #ffffff;
  }
  * { margin: 0; padding: 0; box-sizing: border-box; }
  html, body {
    width: 1200px;
    height: 840px;
    overflow: hidden;
    background: var(--stage);
  }
  .canvas {
    position: relative;
    width: 1200px;
    height: 840px;
  }
  .cover {
    position: absolute;
    left: 300px;
    top: 100px;
    width: 600px;
    height: 640px;
    background: var(--paper);
    overflow: hidden;
    box-shadow: 0 18px 40px rgba(0, 0, 0, 0.18);
  }
  .cover-art {
    position: absolute;
    inset: 0;
    width: 600px;
    height: 640px;
  }
  .headline {
    position: absolute;
    left: 36px;
    top: 300px;
    font-family: "Montserrat", sans-serif;
    font-weight: 800;
    font-size: 34px;
    line-height: 1.02;
    letter-spacing: 0.5px;
    color: var(--text-light);
    text-transform: uppercase;
  }
  .brand {
    position: absolute;
    left: 418px;
    top: 314px;
    display: flex;
    align-items: center;
    gap: 8px;
  }
  .brand-mark {
    width: 12px;
    height: 12px;
    background: var(--brand-green);
  }
  .brand-name {
    font-family: "Montserrat", sans-serif;
    font-weight: 700;
    font-size: 16px;
    letter-spacing: 1px;
    color: var(--brand-blue);
    text-transform: uppercase;
    line-height: 1.1;
  }
</style>
</head>
<body>
<main class="canvas">
  <section class="cover">
    <svg class="cover-art" viewBox="0 0 600 640" xmlns="http://www.w3.org/2000/svg">
      <defs>
        <linearGradient id="handshakeTone" x1="0" y1="0" x2="1" y2="1">
          <stop offset="0" stop-color="#8fa3c2"/>
          <stop offset="0.5" stop-color="#5b6c86"/>
          <stop offset="1" stop-color="#c7d3e4"/>
        </linearGradient>
        <linearGradient id="skylineTone" x1="0" y1="0" x2="1" y2="1">
          <stop offset="0" stop-color="#2f9a4a"/>
          <stop offset="1" stop-color="#146b2c"/>
        </linearGradient>
        <linearGradient id="towerTone" x1="0" y1="0" x2="0.6" y2="1">
          <stop offset="0" stop-color="#4b5565"/>
          <stop offset="0.5" stop-color="#262d3a"/>
          <stop offset="1" stop-color="#121722"/>
        </linearGradient>
      </defs>

      <polygon class="photo-handshake" role="img"
        aria-label="Photo: business handshake over a desk with documents"
        points="0,0 600,0 600,40 385,262 0,185" fill="url(#handshakeTone)"/>

      <polygon class="photo-skyline" role="img"
        aria-label="Photo: city skyline tinted in brand green"
        points="600,78 600,300 428,288" fill="url(#skylineTone)"/>

      <polygon class="photo-tower" role="img"
        aria-label="Photo: glass office tower seen from below"
        points="0,222 392,300 408,640 0,640" fill="url(#towerTone)"/>

      <path class="wave-ground" d="M0,548 Q330,522 600,318 L600,640 L0,640 Z" fill="var(--paper)"/>
      <path class="wave-line" d="M0,548 Q330,522 600,318 L600,330 Q336,536 0,560 Z" fill="var(--brand-green)"/>
      <path class="wave-band" d="M0,572 Q342,548 600,346 L600,640 L0,640 Z" fill="var(--brand-blue)"/>
    </svg>

    <h1 class="headline">We<br>will<br>do the<br>best<br>for your<br>future</h1>

    <div class="brand">
      <span class="brand-mark"></span>
      <span class="brand-name">Velmora<br>Finance</span>
    </div>
  </section>
</main>
</body>
</html>
```